Business Card Design

I need a business card design. I am a sole practitioner.I am a psychotherapist and I need a professional card. I am also an art therapist (a form of psychotherapy using art) so I want the image to be professional/creative/maybe ethnic. I do not want a boring minimalist "medical" image, nor do I want it too hippy/tree hugging.
Colours like reds/ochres/yellows would be good.
Industry/Entity Type
Business
Contact Information for Business Card
Mira Tanvel
Psychotherapy, Counselling and Art Therapy
Korrabel Lodge Counselling and Wellbeing services
17 Farrow Lane, Pelbury 4091
0419362750 www.MiraTanvel.com.au
on rear of card I need the option to have at least 4 or 5 appointment times /dates
Look and feel
Each slider illustrates characteristics of the customer's brand and the style your logo design should communicate.

```html
<!DOCTYPE html>
<html lang="en">
<head>
<meta charset="utf-8">
<title>Mira Tanvel – Business Card</title>
<link rel="stylesheet" href="https://fonts.googleapis.com/css2?family=Andika:wght@400;700&display=swap">
<style>
  :root {
    --backdrop: #e9e4dc;
    --card-dark: #3b3738;
    --band-tan: #b89d6c;
    --gold: #c99a4c;
    --ink: #141212;
    --mark-light: #b5874a;
    --mark-dark: #2f2a27;
  }
  * { margin: 0; padding: 0; box-sizing: border-box; }
  html, body {
    width: 1200px; height: 750px; overflow: hidden;
    background: var(--backdrop);
    font-family: "Andika", "Trebuchet MS", sans-serif;
  }
  .card {
    position: absolute; left: 150px; top: 105px;
    width: 900px; height: 540px;
    background: var(--card-dark);
    border-radius: 4px;
    box-shadow: 0 14px 36px rgba(0,0,0,0.28);
    overflow: hidden;
  }
  .card__band {
    position: absolute; left: 0; top: 0; width: 100%; height: 160px;
    background: var(--band-tan);
  }
  .card__mark {
    position: absolute; left: 42px; top: 62px;
    width: 196px; height: 196px;
    border-radius: 6px;
    background: linear-gradient(135deg, var(--mark-light), var(--mark-dark) 55%, var(--mark-light));
    box-shadow: 0 4px 10px rgba(0,0,0,0.35);
  }
  .card__name {
    position: absolute; left: 268px; top: 52px;
    font-size: 50px; font-weight: 400; color: var(--ink); line-height: 1;
  }
  .card__title {
    position: absolute; left: 272px; top: 116px;
    font-size: 19px; color: var(--ink);
  }
  .contact {
    position: absolute; left: 46px; top: 280px;
    color: var(--gold); list-style: none;
  }
  .contact__phone { font-size: 27px; line-height: 38px; margin-bottom: 8px; }
  .contact__item { font-size: 19px; line-height: 27px; margin-bottom: 6px; }
  .appointments {
    position: absolute; left: 340px; top: 172px; width: 520px;
    color: var(--gold);
  }
  .appointments__heading {
    font-size: 26px; font-weight: 700; line-height: 36px; text-align: center;
    margin-left: 90px; margin-bottom: 14px;
  }
  .appointments__row {
    font-size: 20px; font-weight: 700; line-height: 28px; margin-bottom: 12px;
    white-space: nowrap; text-align: right;
  }
  .rule {
    position: absolute; height: 2px;
    background: var(--gold);
  }
  .rule--upper { top: 400px; left: 330px; right: 40px; }
  .rule--lower { top: 494px; left: 40px; right: 40px; }
  .address {
    position: absolute; left: 0; top: 414px; width: 100%;
    text-align: center; color: var(--gold); font-style: normal;
    font-size: 20px; font-weight: 700; line-height: 30px;
  }
</style>
</head>
<body>
  <section class="card">
    <div class="card__band"></div>
    <div class="card__mark" role="img" aria-label="Decorative square emblem of flowing lines and spirals in gold on dark brown"></div>
    <h1 class="card__name">Mira Tanvel</h1>
    <p class="card__title">Psychotherapy and Counselling</p>

    <ul class="contact">
      <li class="contact__phone">0419 362750</li>
      <li class="contact__item">miratanvel@inbox.com</li>
      <li class="contact__item">www.miratanvel.com.au</li>
    </ul>

    <div class="appointments">
      <h2 class="appointments__heading">Appointment</h2>
      <p class="appointments__row">Date ..../..../........ &nbsp;Time ...........a.m/p.m</p>
      <p class="appointments__row">Date ..../..../........ &nbsp;Time ...........a.m/p.m</p>
      <p class="appointments__row">Date ..../..../........ &nbsp;Time ...........a.m/p.m</p>
      <p class="appointments__row">Date ..../..../........ &nbsp;Time ...........a.m/p.m</p>
    </div>

    <div class="rule rule--upper"></div>
    <address class="address">
      Korrabel Lodge Counselling &amp; Wellbeing Services<br>
      17 Farrow Lane, Pelbury, 4091
    </address>
    <div class="rule rule--lower"></div>
  </section>
</body>
</html>
```